Business Card Design

Hi I need a business card designed, we already have the business name logo artwork and would like some concept ideas for the Bus Card layout.
On the back of the card i want to include the products and services that we offer.
We are a Plastics Sheeting manufacture based in Perth Australia.

                                       

We need a BC design for a company called Tarnby Plastics based in Perth Australia.

We supply from DIY to Trade & Industrial  Engineering Markets.

We specialise in:

·         Cut to size panels  (all shapes and sizes)

·         Plastics fabrication & Welding

·         Custom Designs

·         Plastic Repairs

·         PVC Pipe Slotting & PVC Pipe Threading

·         Supplier of all types of engineering plastics and profiles.

Including:           Acrylic / Vendrix

                               Polycarbonate / Moravite

                               Prismatic Light Diffuser

                               Tubrasin

                               HDPE / UHMWPE

                               PVC / PVC Foam

                               Nylon

                               HIPS

```html
<!DOCTYPE html>
<html lang="en">
<head>
<meta charset="utf-8">
<title>Tarnby Plastics – Business Card</title>
<link href="https://fonts.googleapis.com/css2?family=Open+Sans:wght@400;600;700;800&display=swap" rel="stylesheet">
<style>
  :root {
    --navy: #1d2d6b;
    --navy-text: #1f2f6e;
    --gold: #f3aa1c;
    --orange: #ee7d1a;
    --red: #c8202f;
    --yellow: #f6b81e;
    --white: #ffffff;
    --ink: #3b3b3b;
    --stage: #eceae6;
    --divider: rgba(255,255,255,0.45);
  }
  * { box-sizing: border-box; margin: 0; padding: 0; }
  html, body { width: 1200px; height: 720px; overflow: hidden; }
  body {
    background: var(--stage);
    font-family: "Open Sans", Arial, sans-serif;
    display: flex;
    align-items: center;
    justify-content: center;
    gap: 30px;
  }
  .card {
    width: 560px;
    height: 342px;
    position: relative;
    overflow: hidden;
    box-shadow: 0 4px 14px rgba(0,0,0,0.18);
  }

  /* Front */
  .card-front { background: var(--white); }
  .edge-band { position: absolute; left: 0; top: 0; width: 16px; height: 100%; display: flex; flex-direction: column; }
  .edge-band .red { background: var(--red); flex: 0 0 70px; }
  .edge-band .orange { background: var(--orange); flex: 0 0 150px; }
  .edge-band .yellow { background: var(--yellow); flex: 1; }
  .front-brand {
    position: absolute; left: 42px; top: 34px;
    display: flex; align-items: center; gap: 10px;
  }
  .brand-mark { width: 22px; height: 22px; background: var(--navy); }
  .brand-name { font-weight: 800; font-size: 40px; color: var(--navy); letter-spacing: -0.5px; }
  .holder { position: absolute; right: 34px; top: 128px; text-align: right; }
  .holder-name { font-weight: 700; font-size: 17px; color: var(--navy-text); }
  .holder-title { font-size: 12px; color: var(--orange); }
  .contact { position: absolute; left: 38px; top: 170px; font-size: 12.5px; color: var(--ink); line-height: 21px; }
  .contact-line { display: flex; align-items: center; gap: 6px; }
  .contact-line svg { width: 12px; height: 12px; flex: none; }
  .contact-address { margin-top: 6px; }
  .contact-legal { margin-top: 6px; }

  /* Back */
  .card-back { background: var(--navy); color: var(--white); }
  .back-brand {
    position: absolute; left: 0; right: 0; top: 26px;
    text-align: center; font-weight: 800; font-size: 42px; letter-spacing: -0.5px;
  }
  .tagline { position: absolute; left: 0; right: 0; top: 92px; text-align: center; font-weight: 700; font-size: 13.5px; line-height: 19px; }
  .columns { position: absolute; left: 30px; right: 24px; top: 146px; bottom: 18px; display: flex; }
  .col-services { flex: 0 0 282px; }
  .col-materials { flex: 1; padding-left: 16px; border-left: 1px solid var(--divider); margin-left: 10px; }
  .col-heading { color: var(--gold); font-weight: 700; font-size: 17px; margin-bottom: 4px; }
  .list { list-style: none; font-size: 13px; line-height: 19px; }
  .list li { position: relative; padding-left: 13px; }
  .list li::before,
  .list .inline-item::before {
    content: ""; position: absolute; left: 0; top: 7px;
    width: 6px; height: 6px; border-radius: 50%; background: var(--gold);
  }
  .list .inline-item { position: relative; padding-left: 11px; margin-left: 6px; }
</style>
</head>
<body>

  <section class="card card-front" aria-label="Business card front">
    <div class="edge-band"><span class="red"></span><span class="orange"></span><span class="yellow"></span></div>
    <div class="front-brand">
      <span class="brand-mark"></span>
      <span class="brand-name">Tarnby Plastics</span>
    </div>
    <div class="holder">
      <div class="holder-name">Your Name</div>
      <div class="holder-title">Title</div>
    </div>
    <div class="contact">
      <div class="contact-line">
        <svg viewBox="0 0 12 12"><path d="M2 1h3l1 3-2 1a7 7 0 0 0 3 3l1-2 3 1v3c-6 0-9-3-9-9z" fill="var(--orange)"/></svg>
        <span>08 5550 1184</span>
      </div>
      <div class="contact-line">
        <svg viewBox="0 0 12 12"><rect x="3" y="0.5" width="6" height="11" rx="1" fill="var(--orange)"/><rect x="4" y="2" width="4" height="6" fill="var(--white)"/></svg>
        <span>0400 555 731</span>
      </div>
      <div class="contact-line">
        <svg viewBox="0 0 12 12"><rect x="1" y="4" width="10" height="6" rx="1" fill="var(--orange)"/><rect x="3" y="1" width="6" height="3" fill="var(--orange)"/></svg>
        <span>08 5550 1185</span>
      </div>
      <div class="contact-line">
        <svg viewBox="0 0 12 12"><rect x="0.5" y="2" width="11" height="8" rx="1" fill="var(--orange)"/><path d="M1 3l5 4 5-4" stroke="var(--white)" fill="none"/></svg>
        <span>sales@tarnbyplastics.com.au</span>
      </div>
      <div class="contact-address">
        Unit 4/18 Kestrel Loop Ridgemont WA 6158<br>
        PO Box 2274 Ridgemont DC WA 6971
      </div>
      <div class="contact-legal">Harlow Vale Pty Ltd T/A Tarnby Plastics ABN: TBA</div>
    </div>
  </section>

  <section class="card card-back" aria-label="Business card back">
    <div class="back-brand">Tarnby Plastics</div>
    <p class="tagline">The Products And Services That We Offer<br>Are Supplied From Diy To Trade &amp; Industrial Engineering Markets</p>
    <div class="columns">
      <div class="col-services">
        <h3 class="col-heading">We specialise in:</h3>
        <ul class="list">
          <li>Cut to size panels (all shapes and sizes)</li>
          <li>Plastics fabrication &amp; Welding</li>
          <li>Custom Designs</li>
          <li>Plastic Repairs</li>
          <li>PVC Pipe Slotting &amp; PVC Pipe Threading</li>
          <li>Supplier of all types of engineering plastics and profiles</li>
        </ul>
      </div>
      <div class="col-materials">
        <h3 class="col-heading">Including:</h3>
        <ul class="list">
          <li>Acrylic / Vendrix</li>
          <li>Polycarbonate / Moravite</li>
          <li>Prismatic Light Diffuser</li>
          <li>Tubrasin<span class="inline-item">HDPE / UHMWPE</span></li>
          <li>PVC / PVC Foam</li>
          <li>Nylon<span class="inline-item">HIPS</span></li>
        </ul>
      </div>
    </div>
  </section>

</body>
</html>
```